Website Header Design

Hi,

We're an electrical company that is looking for a new website header.
Our website is www.brantwoodvoltage.com
We are located in Toronto, Ontario, Canada.
We perform a lot of high rise electrical service work, snow melting system installation in garage ramps, and other general electrical work.
We're willing to change the size of the header and location/look of menus if needed but it is not required. We are hoping to keep our slogan if possible but having it in the header is not a make or break item. Whatever looks better.

Maybe the Toronto skyline could be incorporated somehow but the header also has to have some relevance to an electrical company.
I uploaded png files of the logo but I also have vector files available if needed

Target Market(s)

Property Managers, Contractors, Consulting Engineers

Industry/Entity Type

Electrical

Requirements
Must have
• Our Logo.
Nice to have
• Slogan
Should not have
• Flash

```html
<!DOCTYPE html>
<html lang="en">
<head>
<meta charset="utf-8">
<title>Brantwood Voltage — Website Header</title>
<link rel="stylesheet" href="https://fonts.googleapis.com/css2?family=Source+Sans+3:wght@400;600&family=Arimo:wght@400;700&display=swap">
<style>
  :root {
    --page-bg: #ffffff;
    --banner-black: #000000;
    --slogan-grey: #d9d9d9;
    --brand-white: #ffffff;
    --brand-mark: #f39a1e;
    --button-top: #5a5a5a;
    --button-mid: #262626;
    --button-bottom: #0d0d0d;
    --button-edge: #8a8a8a;
    --sky-violet: #6b6fb8;
    --sky-blue: #9aa4e0;
    --sky-rose: #b0526a;
    --city-dark: #1c2038;
  }
  * { margin: 0; padding: 0; box-sizing: border-box; }
  html, body {
    width: 1200px;
    height: 261px;
    overflow: hidden;
    background: var(--page-bg);
  }
  .header-canvas {
    position: relative;
    width: 1200px;
    height: 261px;
  }
  .banner {
    position: absolute;
    left: 23px;
    top: 19px;
    width: 1104px;
    height: 220px;
    background: var(--banner-black);
    overflow: hidden;
  }
  .skyline-photo {
    position: absolute;
    left: 470px;
    top: 0;
    width: 648px;
    height: 220px;
    background:
      linear-gradient(to right, var(--banner-black) 0%, rgba(0,0,0,0) 28%),
      linear-gradient(to bottom, rgba(0,0,0,0) 60%, var(--city-dark) 78%, #0a0a12 100%),
      radial-gradient(ellipse at 70% 30%, #e8ecff 0%, var(--sky-blue) 25%, var(--sky-violet) 55%, rgba(107,111,184,0) 80%),
      linear-gradient(100deg, var(--sky-rose) 0%, #4a4f8e 40%, var(--sky-violet) 100%);
  }
  .brand {
    position: absolute;
    left: 38px;
    top: 20px;
    width: 180px;
    text-align: center;
  }
  .brand-square {
    display: block;
    width: 72px;
    height: 72px;
    margin: 12px auto 16px;
    background: var(--brand-mark);
  }
  .brand-name {
    font-family: "Source Sans 3", sans-serif;
    font-weight: 600;
    font-size: 30px;
    line-height: 32px;
    color: var(--brand-white);
  }
  .slogan {
    position: absolute;
    left: 186px;
    top: 44px;
    font-family: "Source Sans 3", sans-serif;
    font-weight: 600;
    font-size: 49px;
    line-height: 46px;
    letter-spacing: -0.5px;
    color: var(--slogan-grey);
  }
  .main-nav {
    position: absolute;
    top: 163px;
    left: 0;
    width: 100%;
    height: 46px;
  }
  .nav-button {
    position: absolute;
    top: 0;
    height: 45px;
    border-radius: 9px;
    border: 1px solid var(--button-edge);
    background: linear-gradient(to bottom, var(--button-top) 0%, var(--button-mid) 50%, var(--button-bottom) 100%);
    font-family: "Arimo", sans-serif;
    font-size: 27px;
    line-height: 43px;
    letter-spacing: -1.5px;
    color: var(--brand-white);
    text-align: center;
    text-decoration: none;
  }
  .nav-button.is-current { font-weight: 700; letter-spacing: -1px; }
</style>
</head>
<body>
<div class="header-canvas">
  <header class="banner">
    <div class="skyline-photo" role="img" aria-label="Photograph of the Toronto skyline at dusk under a violet sky crossed by glowing network lines"></div>

    <div class="brand">
      <span class="brand-square"></span>
      <div class="brand-name">Brantwood<br>Voltage</div>
    </div>

    <p class="slogan">Powerful Solutions.<br>Professional Service.</p>

    <nav class="main-nav">
      <a class="nav-button is-current" href="#" style="left:229px;width:122px;">Home</a>
      <a class="nav-button" href="#" style="left:371px;width:130px;">About us</a>
      <a class="nav-button" href="#" style="left:513px;width:125px;">Services</a>
      <a class="nav-button" href="#" style="left:654px;width:126px;">Projects</a>
      <a class="nav-button" href="#" style="left:795px;width:125px;">Clients</a>
      <a class="nav-button" href="#" style="left:925px;width:142px;">Contact us</a>
    </nav>
  </header>
</div>
</body>
</html>
```